Web Design Project

Need a web design to be built by in-house team of developers. I need the look and feel of the site done ready for the developers to take over.

The site is a crowd funding site like www.pennyharbor.example. Our site will have all the main functions provided for on this site.
We are not looking for sophisticated investors, instead we are looking for people with an interest in investing but that need a lot of help and support through the process.

I have already obtained the logo. I attach it here.

I also want to have a coming soon page designed. I have sketched out what i want here and am uploading it in excel. this is obviously very basic and not what i will want for the main site.

colours should be light and accessible: blues, greens, yellows.

Site is to be fun and accessible.

site will have a lot of communication based aspects needed.

I am looking for a long term relationship with a designer to do this and to do many more things. I will have a lot of banners and desgin work to do here, and am looking ONLY for someone that can work on an ongoing basis (not full time, but a few hours a week).

I am also after an animation - basic 2 minute intro - not full animation, part powerpoint and part animation. I have made a separate tender for this, please quote me on it. I want the same person doing them all preferably....
Updates

Hi all

I am impressed with some of these designs. I have uploaded the wireframe of the coming soon page. 

I prefer the designs so far that are utilizing our little icons etc. 

obviously i understand you havent got root access or anything yet so are struggling to put them in, but its worth a try, some of the designs are using them well. 

i like bright colours. 

i would also show me how you are going to design other aspects eg chat box, forum page etc. 

Reason: i am going to choose a short list today and then deal only with those to get the final designs done.

Industry/Entity Type

Communication

Requirements
Must have
• the site will have all the functions of www.pennyharbor.example and www.backlantern.example.

```html
<!DOCTYPE html>
<html lang="en">
<head>
<meta charset="utf-8">
<title>Fundora – Equity Crowdfunding</title>
<link href="https://fonts.googleapis.com/css2?family=Arimo:wght@400;700&display=swap" rel="stylesheet">
<style>
:root{
  --frame-blue:#3e6f9e;
  --frame-blue-light:#5b8fc0;
  --nav-dark:#2f4f78;
  --nav-light:#4f77a3;
  --brand-blue:#1d6497;
  --heading-blue:#2c5a8a;
  --panel-blue:#0d5f95;
  --panel-blue-light:#1a8bc6;
  --orange:#f7a21b;
  --orange-light:#ffd36b;
  --yellow:#ffe14a;
  --text-grey:#4a4a4a;
  --line-grey:#c9c9c9;
  --bar-blue:#1b86c2;
  --page:#ffffff;
}
*{margin:0;padding:0;box-sizing:border-box}
html,body{width:1200px;height:900px;overflow:hidden;background:#fff}
body{font-family:"Arimo",Arial,sans-serif;position:relative;color:var(--text-grey)}
.abs{position:absolute}
.frame{left:243px;top:0;width:712px;height:900px;background:linear-gradient(90deg,var(--frame-blue) 0%,var(--frame-blue-light) 12%,var(--frame-blue) 50%,var(--frame-blue-light) 88%,var(--frame-blue) 100%)}
.page{left:329px;top:0;width:532px;height:900px;background:var(--page)}
/* header */
.header{left:329px;top:0;width:532px;height:48px;background:linear-gradient(#fff,#dcdcdc)}
.logo{left:352px;top:8px;display:flex;align-items:center;gap:5px;font-size:15px;font-weight:700;color:var(--brand-blue)}
.logo-mark{width:12px;height:12px;background:var(--orange)}
.account{left:679px;top:4px;font-size:7px;font-weight:700;color:var(--heading-blue)}
.social-signin{left:745px;top:2px;width:95px;height:14px;border:1px solid #9ab;background:#fff;display:flex;align-items:center;gap:3px;padding-left:2px;font-size:6.5px;font-weight:700;color:var(--heading-blue)}
.social-signin i{width:10px;height:10px;background:#3b5998;display:block}
.nav{left:329px;top:50px;width:532px;height:21px;background:linear-gradient(var(--nav-light),var(--nav-dark));display:flex;justify-content:flex-end;gap:13px;padding-right:21px;align-items:center;font-size:7px;font-weight:700;color:#fff}
.nav .current{color:var(--yellow)}
/* intro */
.intro{left:329px;top:71px;width:532px;height:48px;background:linear-gradient(#fff,#eaeaea)}
.tagline{left:351px;top:83px;font-size:10.5px;font-weight:700;color:var(--brand-blue)}
.subline{left:351px;top:99px;font-size:9px;font-weight:700;color:#555}
.learn{left:765px;top:99px;font-size:9px;font-weight:700;color:var(--brand-blue)}
.press{left:340px;top:119px;width:511px;height:24px;border:1px solid #888;border-radius:3px;background:#fff;display:flex;align-items:center;gap:9px;padding-left:22px}
.press span{font-size:6px;font-weight:700;color:#555;margin-right:4px}
.press i{display:block;height:11px;background:#d8d8d8}
/* promos */
.promo{left:339px;width:150px;height:53px;border:1px solid #aaa}
.promo-photo{width:100%;height:100%}
.promo-label{left:6px;top:4px;font-size:7px;font-weight:700;color:#333;background:rgba(255,255,255,.7);padding:1px 2px}
.promo-btn{left:8px;top:34px;font-size:6px;font-weight:700;padding:2px 3px;border-radius:2px}
.banner{left:495px;top:148px;width:356px;height:110px;border:1px solid #7b3;background:linear-gradient(100deg,#b9e35a,#5aa823 55%,#9bd247)}
.banner-photo{left:200px;top:0;width:155px;height:108px;background:radial-gradient(circle at 60% 40%,#e3d9c4,#6d9e3a 70%)}
.banner-title{left:12px;top:20px;font-size:10px;font-weight:700;color:#111}
.banner-copy{left:12px;top:38px;width:175px;font-size:5px;line-height:6.5px;color:#000}
.banner-meta{left:12px;top:74px;font-size:6.5px;font-weight:700;color:#000;line-height:8px}
.banner-more{left:92px;top:82px;font-size:6px;font-weight:700;color:#000}
/* sidebar */
.social-row{left:339px;top:272px;width:150px;height:17px;border:1px solid #ccd;display:flex;align-items:center;gap:4px;padding-left:14px;font-size:5.5px;color:#333}
.chip{border:1px solid #99a;padding:1px 3px;background:#eef}
.gap{width:38px}
.video{left:339px;top:294px;width:150px;height:95px;border:2px solid var(--panel-blue);background:var(--panel-blue-light)}
.video-title{left:4px;top:1px;font-size:6px;font-weight:700;color:#fff}
.video-screen{left:2px;top:11px;width:142px;height:64px;background:#fff;display:flex;flex-direction:column;align-items:center;justify-content:center;gap:3px;font-weight:700;color:var(--brand-blue)}
.video-screen b{font-size:12px}
.video-screen small{font-size:8px;color:var(--panel-blue-light)}
.video-play{left:63px;top:30px;width:20px;height:16px;background:rgba(0,0,0,.5);border-radius:3px}
.video-bar{left:2px;top:79px;width:142px;height:8px;background:#ddd}
.newsletter{left:339px;top:395px;width:150px;height:37px;background:linear-gradient(var(--panel-blue-light),var(--panel-blue));border-radius:2px}
.newsletter h3{left:6px;top:3px;font-size:9px;color:#fff;font-weight:400}
.nl-input{left:6px;top:18px;width:93px;height:12px;background:#ccd;border-radius:2px}
.nl-btn{left:104px;top:18px;width:41px;height:12px;background:linear-gradient(var(--orange-light),var(--orange));font-size:6px;font-weight:700;color:#333;text-align:center;line-height:12px;border-radius:2px}
.blog{left:339px;top:437px;width:150px;height:257px;background:linear-gradient(var(--panel-blue-light),var(--panel-blue) 25%);border-radius:2px;color:#fff}
.blog h3{left:9px;top:6px;font-size:9.5px}
.post{left:9px;width:135px;font-size:6.5px;line-height:8.5px}
.post .date{display:inline-block;background:var(--orange);color:#222;font-weight:700;padding:1px 5px;margin-bottom:4px}
.post b{display:block;margin-bottom:5px}
.post .more{display:block;margin-top:4px;color:var(--yellow);font-size:6px}
.rule{left:9px;width:135px;height:1px;background:#3fb0e6}
.blog-foot{left:9px;top:202px;width:135px;font-size:6px;color:var(--yellow);display:flex;justify-content:space-between}
.follow{left:9px;top:228px;width:80px;height:22px;background:linear-gradient(var(--orange-light),var(--orange));border:1px solid #fff;font-size:8px;font-weight:700;color:#fff;display:flex;align-items:center;justify-content:center}
.about{left:339px;top:700px;width:150px;height:101px;background:linear-gradient(#ffe28a,var(--orange));border:1px solid #e8a030;padding:6px 9px}
.about h3{font-size:9.5px;color:#333;margin-bottom:4px}
.about p{font-size:6px;line-height:8px;color:#222}
.about .more{display:block;margin-top:5px;font-size:6px;color:#222}
/* pitches */
.pitches-h{left:499px;top:273px;font-size:12px;font-weight:700;color:var(--heading-blue)}
.pitches-rule{left:495px;top:287px;width:356px;height:2px;background:var(--heading-blue)}
.btn-more{width:48px;height:12px;background:linear-gradient(var(--orange-light),var(--orange));font-size:6.5px;font-weight:700;color:#333;text-align:center;line-height:12px}
.pitch{width:160px;height:156px}
.pitch h4{left:0;top:1px;font-size:8px;color:var(--heading-blue);font-weight:700}
.pitch-photo{left:0;top:16px;width:68px;height:68px;background:linear-gradient(135deg,#b9c8dc,#4d6f9f)}
.pitch-copy{left:74px;top:17px;width:84px;font-size:5px;line-height:7.2px;color:#111}
.pitch-tail{left:2px;top:88px;font-size:5px;color:#111}
.progress{left:0;top:104px;width:158px;height:31px;background:#e2e2e2;border-radius:2px}
.progress i{position:absolute;left:7px;top:7px;width:9px;height:8px;background:var(--orange)}
.progress em{position:absolute;left:17px;top:6px;width:133px;height:9px;background:linear-gradient(#6fc4ec,var(--bar-blue) 50%,#0f5e8e)}
.progress span{position:absolute;left:5px;top:19px;font-size:7.5px;font-weight:700;color:#222}
.progress span b{color:var(--orange)}
.pitch-rule{left:0;top:145px;width:158px;height:1px;background:var(--heading-blue)}
.pitches-end{left:499px;top:754px;width:341px;height:2px;background:var(--heading-blue)}
/* footer */
.footer{left:329px;top:812px;width:532px;height:79px;border-top:1px solid var(--heading-blue);background:linear-gradient(#fff,#d6d6d6)}
.footer-links{left:10px;top:15px;font-size:6.5px;color:var(--heading-blue)}
.footer-note{left:10px;top:32px;font-size:6.5px;line-height:8px;color:var(--heading-blue)}
.footer-copy{left:10px;top:57px;font-size:6.5px;color:var(--heading-blue)}
</style>
</head>
<body>
<div class="abs frame"></div>
<div class="abs page"></div>

<header class="abs header"></header>
<div class="abs logo"><span class="logo-mark"></span>Fundora</div>
<div class="abs account">Log in &nbsp;|&nbsp; Sign up</div>
<div class="abs social-signin"><i></i>Sign in with Friendnet</div>
<nav class="abs nav"><span class="current">Invest</span><span>Get Investment</span><span>How it works</span><span>About us</span><span>Blog</span><span>Forum</span></nav>

<section class="abs intro"></section>
<div class="abs tagline">A new way to invest...</div>
<div class="abs subline">The world's first equity-based crowdfunding community dedicated to business investment</div>
<div class="abs learn">➡ Learn more</div>
<div class="abs press"><span>FEATURED IN</span><i style="width:44px"></i><i style="width:66px"></i><i style="width:48px"></i><i style="width:30px"></i><i style="width:46px"></i><i style="width:44px"></i><i style="width:64px"></i></div>

<div class="abs promo" style="top:148px">
  <div class="promo-photo" role="img" aria-label="Photo of stacked coins" style="background:linear-gradient(120deg,#7a4a2a,#d39b6a,#8a5a3a)"></div>
  <div class="abs promo-label">Invest in a business</div>
  <div class="abs promo-btn" style="background:var(--panel-blue-light);color:#fff">Search pitches now</div>
</div>
<div class="abs promo" style="top:205px">
  <div class="promo-photo" role="img" aria-label="Photo of a hand signing a document" style="background:linear-gradient(120deg,#f2e3d6,#e8b9a0,#f6eee8)"></div>
  <div class="abs promo-label">Get Investment for your business</div>
  <div class="abs promo-btn" style="background:var(--yellow);color:#333">Get investment now</div>
</div>

<div class="abs banner">
  <div class="abs banner-photo" role="img" aria-label="Photo of a businesswoman drawing a pie chart"></div>
  <div class="abs banner-title">Blog Title text will go here.</div>
  <div class="abs banner-copy">Text will go here. Text will go here. Text will go here. Text will go here. Text will go here. Text will go here. Text will go here. Text will go here. Text will go here. Text will go here.</div>
  <div class="abs banner-meta">Loram<br>Ipsum</div>
  <div class="abs banner-more">Click for more information</div>
</div>

<div class="abs social-row"><span class="chip">Like</span><span class="chip">302</span><span class="gap"></span><span class="chip">Chirp</span><span>257</span></div>
<div class="abs video">
  <div class="abs video-title">Fundora - How it works</div>
  <div class="abs video-screen"><b>Fundora</b><small>How it Works</small></div>
  <div class="abs video-play"></div>
  <div class="abs video-bar"></div>
</div>
<div class="abs newsletter"><h3 class="abs">Newsletter</h3><div class="abs nl-input"></div><div class="abs nl-btn">Subscribe</div></div>
<aside class="abs blog">
  <h3 class="abs">Latest from our Blog</h3>
  <div class="abs post" style="top:27px"><span class="date">21.08.2011</span><b>Headline will go here. Headline will go here.</b>Normal text will go here. Normal text will go here. Normal text will go here. Normal text will go here. Normal text will go here.<span class="more">➡ read more</span></div>
  <div class="abs rule" style="top:105px"></div>
  <div class="abs post" style="top:116px"><span class="date">21.08.2011</span><b>Headline will go here. Headline will go here.</b>Normal text will go here. Normal text will go here. Normal text will go here. Normal text will go here. Normal text will go here.<span class="more">➡ read more</span></div>
  <div class="abs rule" style="top:194px"></div>
  <div class="abs blog-foot"><span>➡ see more posts</span><span>RSS ▪</span></div>
  <div class="abs follow">Follow us on Chirper</div>
</aside>
<aside class="abs about">
  <h3>What is Fundora funding?</h3>
  <p>Fundorafunding is the new way for a community of like minded people to network and pool their money and knowledge together. Fundora provides a platform for entrepreneurs of start-ups and established businesses to connect with potential investors.</p>
  <span class="more">➡ read more</span>
</aside>

<h2 class="abs pitches-h">Featured pitches</h2>
<div class="abs btn-more" style="left:796px;top:273px">view more</div>
<div class="abs pitches-rule"></div>

<article class="abs pitch" style="left:499px;top:296px"><h4 class="abs">Real World Gallery</h4><div class="abs pitch-photo" role="img" aria-label="Collage of business people photos"></div><p class="abs pitch-copy">Text will go here. Text will go here. Text will go here. Text will go here. Text will go here. Text will go here. Text will go here. Text will go here.</p><p class="abs pitch-tail">Text will go here. Text will</p><div class="abs progress"><i></i><em></em><span><b>10%</b> invested so far</span></div><div class="abs pitch-rule"></div></article>
<article class="abs pitch" style="left:681px;top:296px"><h4 class="abs">Real World Gallery</h4><div class="abs pitch-photo" role="img" aria-label="Collage of business people photos"></div><p class="abs pitch-copy">Text will go here. Text will go here. Text will go here. Text will go here. Text will go here. Text will go here. Text will go here. Text will go here.</p><p class="abs pitch-tail">Text will go here. Text will</p><div class="abs progress"><i></i><em></em><span><b>10%</b> invested so far</span></div><div class="abs pitch-rule"></div></article>
<article class="abs pitch" style="left:499px;top:452px"><h4 class="abs">Real World Gallery</h4><div class="abs pitch-photo" role="img" aria-label="Collage of business people photos"></div><p class="abs pitch-copy">Text will go here. Text will go here. Text will go here. Text will go here. Text will go here. Text will go here. Text will go here. Text will go here.</p><p class="abs pitch-tail">Text will go here. Text will</p><div class="abs progress"><i></i><em></em><span><b>10%</b> invested so far</span></div><div class="abs pitch-rule"></div></article>
<article class="abs pitch" style="left:681px;top:452px"><h4 class="abs">Real World Gallery</h4><div class="abs pitch-photo" role="img" aria-label="Collage of business people photos"></div><p class="abs pitch-copy">Text will go here. Text will go here. Text will go here. Text will go here. Text will go here. Text will go here. Text will go here. Text will go here.</p><p class="abs pitch-tail">Text will go here. Text will</p><div class="abs progress"><i></i><em></em><span><b>10%</b> invested so far</span></div><div class="abs pitch-rule"></div></article>
<article class="abs pitch" style="left:499px;top:608px"><h4 class="abs">Real World Gallery</h4><div class="abs pitch-photo" role="img" aria-label="Collage of business people photos"></div><p class="abs pitch-copy">Text will go here. Text will go here. Text will go here. Text will go here. Text will go here. Text will go here. Text will go here. Text will go here.</p><p class="abs pitch-tail">Text will go here. Text will</p><div class="abs progress"><i></i><em></em><span><b>10%</b> invested so far</span></div></article>
<article class="abs pitch" style="left:681px;top:608px"><h4 class="abs">Real World Gallery</h4><div class="abs pitch-photo" role="img" aria-label="Collage of business people photos"></div><p class="abs pitch-copy">Text will go here. Text will go here. Text will go here. Text will go here. Text will go here. Text will go here. Text will go here. Text will go here.</p><p class="abs pitch-tail">Text will go here. Text will</p><div class="abs progress"><i></i><em></em><span><b>10%</b> invested so far</span></div></article>
<div class="abs pitches-end"></div>
<div class="abs btn-more" style="left:796px;top:761px">view more</div>

<footer class="abs footer">
  <div class="abs footer-links">Contact us &nbsp;|&nbsp; Terms of Use &nbsp;|&nbsp; Privacy policy &nbsp;|&nbsp; Sitemap &nbsp;|&nbsp; FAQ &nbsp;|&nbsp; Partnership Opportunities &nbsp;|&nbsp; Press</div>
  <div class="abs footer-note">This website has been approved as a financial promotion by Harlow Mercer which is authorised and<br>regulated by the Financial Conduct Board.</div>
  <div class="abs footer-copy">Copyright 2011-2012 &nbsp;Fundora Limited All right reserved.</div>
</footer>
</body>
</html>
```